Promotional Poster for Music Achievement Program

I need a vertical 11x17 poster designed for a new program called Bright Steps Music Achievement Program. The poster will be displayed in the lesson rooms and lobbies of music schools who use this program. The main headline of the flyer should be "Ask your teacher about Bright Steps" And then the additional text should be "Love your lessons and practice like never before with 10 levels of achievement!" I would like to use the logo on the flyer, which I uploaded here. In terms of artwork/design, I am looking for a fun, but clean feel. The purpose of the program is for students to progress through ten levels of achievement as they climb higher and higher to mastery of their instrument at level 10, so a feel of climbing, leveling up, or advancing would be good. And of course, this is a music program, so any musical artwork involved would make sense. But again - nothing too busy or overwhelming!

Target Market(s)

Parents waiting in the lobby of a music school.

Industry/Entity Type

Promotional

Colors

Designer to choose colors to be used in the design.

Requirements
Must have
• - Bright Steps logo
• - This headline: Ask your teacher about Bright Steps
• - This additional text: Love your lessons and practice like never before with 10 levels of achievement!
Nice to have
• In terms of artwork/design, I am looking for a fun, but clean feel. The purpose of the program is for students to progress through ten levels of achievement as they climb higher and higher to mastery of their instrument at level 10, so a feel of climbing, leveling up, or advancing would be good. And of course, this is a music program, so any musical artwork involved would make sense. But again - nothing too busy or overwhelming!
Should not have
• Should not be too busy.

```html
<!DOCTYPE html>
<html lang="en">
<head>
<meta charset="utf-8">
<title>Bright Steps Music Achievement Program Poster</title>
<link rel="stylesheet" href="https://fonts.googleapis.com/css2?family=Roboto:wght@400;500;700;900&display=swap">
<style>
  :root {
    --stage: #3d3d3d;
    --paper: #ffffff;
    --ink: #1a1a1a;
    --band: #2b2420;
    --amber: #ef900f;
    --amber-soft: #f4a833;
    --lime: #c5d92d;
    --red: #e8202e;
  }
  * { margin: 0; padding: 0; box-sizing: border-box; }
  html, body { width: 1200px; height: 1200px; overflow: hidden; }
  body { background: var(--stage); font-family: "Roboto", Arial, sans-serif; }
  .poster-frame {
    position: absolute; left: 210px; top: 48px;
    width: 780px; height: 1104px; overflow: hidden;
  }
  .poster {
    position: absolute; left: 0; top: 0;
    width: 768px; height: 1087px;
    transform: scale(1.0156); transform-origin: 0 0;
    background: var(--paper);
  }
  .poster-art { position: absolute; inset: 0; width: 768px; height: 1087px; }
  .brand {
    position: absolute; left: 0; right: 0; top: 64px;
    display: flex; justify-content: center; align-items: center; gap: 16px;
  }
  .brand-mark { width: 34px; height: 34px; background: var(--amber); }
  .brand-name {
    font-family: "Roboto", Arial, sans-serif; font-weight: 700;
    font-size: 52px; color: var(--ink); letter-spacing: -0.5px;
  }
  .headline text { font-family: "Roboto", Arial, sans-serif; fill: #fff; }
  .headline .soft { font-weight: 400; font-size: 50px; }
  .headline .strong { font-weight: 900; font-size: 78px; }
  .headline .accent { fill: var(--lime); }
  .pitch {
    position: absolute; left: 272px; width: 400px; top: 708px;
    text-align: center; color: var(--ink); text-transform: uppercase;
    line-height: 1.2;
  }
  .pitch .line { display: block; font-size: 27px; font-weight: 400; }
  .pitch .love { color: var(--red); font-weight: 500; }
  .pitch .levels { display: block; color: var(--red); font-weight: 700; font-size: 60px; line-height: 1.05; margin-top: 2px; }
  .pitch .closing { display: block; font-size: 35px; font-weight: 400; }
</style>
</head>
<body>
<div class="poster-frame">
  <div class="poster">
    <svg class="poster-art" viewBox="0 0 768 1087" xmlns="http://www.w3.org/2000/svg">
      <defs>
        <linearGradient id="staffGrey" x1="0" y1="0" x2="1" y2="1">
          <stop offset="0" stop-color="#d9d9d9" stop-opacity="0.55"/>
          <stop offset="1" stop-color="#ffffff" stop-opacity="0"/>
        </linearGradient>
        <radialGradient id="staffRed" cx="0" cy="0.3" r="1">
          <stop offset="0" stop-color="#f7b8bb" stop-opacity="0.6"/>
          <stop offset="1" stop-color="#ffffff" stop-opacity="0"/>
        </radialGradient>
        <linearGradient id="meterTones" x1="0" y1="0" x2="1" y2="0">
          <stop offset="0" stop-color="#c5d92d"/>
          <stop offset="0.5" stop-color="#f4a833"/>
          <stop offset="1" stop-color="#e8202e"/>
        </linearGradient>
        <linearGradient id="meterFade" x1="0" y1="0" x2="0" y2="1">
          <stop offset="0" stop-color="#fff" stop-opacity="0"/>
          <stop offset="1" stop-color="#fff" stop-opacity="1"/>
        </linearGradient>
        <mask id="meterMask">
          <rect x="0" y="961" width="768" height="118" fill="url(#meterFade)"/>
        </mask>
      </defs>

      <rect class="music-notes-top" x="0" y="0" width="768" height="300" fill="url(#staffGrey)" role="img" aria-label="Faint grey sweep of music staff lines with clefs and notes"/>
      <rect class="music-notes-bottom" x="0" y="620" width="320" height="360" fill="url(#staffRed)" role="img" aria-label="Soft red sweep of music staff lines with notes"/>

      <polygon class="amber-wedge" points="0,184 371,295 0,404" fill="var(--amber)"/>
      <polygon class="amber-wedge" points="768,500 768,708 380,603" fill="var(--amber)"/>
      <polygon class="headline-band" points="0,404 768,179 768,500 0,704" fill="var(--band)"/>

      <g class="band-stripes" stroke="#fff" stroke-width="3">
        <line x1="0" y1="392" x2="345" y2="291"/>
        <line x1="0" y1="382" x2="320" y2="288"/>
        <line x1="410" y1="607" x2="768" y2="512"/>
        <line x1="440" y1="612" x2="768" y2="524"/>
      </g>

      <g class="headline" transform="rotate(-16 44 524)">
        <text x="44" y="524"><tspan class="soft">ASK YOUR </tspan><tspan class="strong">TEACHER</tspan></text>
        <text x="74" y="616" class="strong" style="font-size:64px">ABOUT BRIGHT <tspan class="accent">STEPS</tspan></text>
      </g>

      <rect class="level-meter" x="8" y="961" width="752" height="118" fill="url(#meterTones)" mask="url(#meterMask)" opacity="0.85" role="img" aria-label="Decorative row of rising sound level bars in lime, amber and red"/>
    </svg>

    <div class="brand">
      <span class="brand-mark"></span>
      <span class="brand-name">Bright Steps</span>
    </div>

    <p class="pitch">
      <span class="line"><span class="love">Love</span> your lessons</span>
      <span class="line">and practice like</span>
      <span class="line">never before with</span>
      <span class="levels">10 Levels</span>
      <span class="closing">of achievement</span>
    </p>
  </div>
</div>
</body>
</html>
```